LumaMove In-home Personal Training

I would like to have some eye-catching business card design. Opened to any ideas.

The business idea: mobile fitness - train clients at their places

Target Market(s)

General population, 20-60 years old

Industry/Entity Type

Fitness

Contact Information for Business Card

The information to include:
Name: Marta
Call or text: 306-555-0187
Website: LumaMove.ca
Please use the attached logo

Requirements
Should not have
• No orange or purple colours please

```html
<!DOCTYPE html>
<html lang="en">
<head>
<meta charset="utf-8">
<title>LumaMove – Business Card</title>
<link rel="stylesheet" href="https://fonts.googleapis.com/css2?family=Montserrat:wght@300;400&family=Work+Sans:wght@400;500&display=swap">
<style>
  :root {
    --page-bg: #d9d9db;
    --card-dark: #4a4a4c;
    --card-light: #ffffff;
    --ink-light: #ffffff;
    --ink-dark: #2b2b2d;
    --rule: #3a3a3c;
    --shadow: rgba(0, 0, 0, 0.18);
  }
  * { margin: 0; padding: 0; box-sizing: border-box; }
  html, body {
    width: 1200px;
    height: 900px;
    overflow: hidden;
    background: var(--page-bg);
  }
  .canvas {
    position: relative;
    width: 1200px;
    height: 900px;
  }
  .card {
    position: absolute;
    left: 300px;
    width: 600px;
    height: 343px;
    border-radius: 26px;
    box-shadow: 0 10px 30px var(--shadow);
    overflow: hidden;
  }
  .card--front { top: 72px; background: var(--card-dark); color: var(--ink-light); }
  .card--back { top: 485px; background: var(--card-light); color: var(--ink-dark); }

  .brand {
    position: absolute;
    display: flex;
    align-items: center;
    gap: 18px;
  }
  .brand__mark {
    border: 2px solid currentColor;
    border-radius: 4px;
    flex: none;
  }
  .brand__text { display: flex; flex-direction: column; }
  .brand__name {
    font-family: "Montserrat", sans-serif;
    font-weight: 300;
    line-height: 1;
    letter-spacing: 0.14em;
  }
  .brand__tagline {
    font-family: "Montserrat", sans-serif;
    font-weight: 300;
    text-transform: uppercase;
    letter-spacing: 0.28em;
    margin-top: 8px;
  }

  .card--front .brand { left: 78px; top: 130px; }
  .card--front .brand__mark { width: 58px; height: 58px; }
  .card--front .brand__name { font-size: 54px; }
  .card--front .brand__tagline { font-size: 10.5px; }

  .card--back .brand { right: 44px; top: 52px; }
  .card--back .brand__mark { width: 36px; height: 36px; border-width: 1.5px; }
  .card--back .brand__name { font-size: 32px; }
  .card--back .brand__tagline { font-size: 6.5px; margin-top: 5px; }

  .card__rule {
    position: absolute;
    left: 40px;
    right: 40px;
    top: 132px;
    height: 1px;
    background: var(--rule);
  }

  .contact {
    position: absolute;
    left: 40px;
    bottom: 34px;
    font-family: "Work Sans", sans-serif;
  }
  .contact__name { font-size: 24px; font-weight: 400; line-height: 1.1; }
  .contact__role { font-size: 11px; margin-top: 2px; }
  .contact__divider {
    width: 140px;
    height: 1px;
    background: var(--rule);
    margin: 10px 0 10px;
  }
  .contact__line {
    display: flex;
    align-items: center;
    gap: 9px;
    font-size: 14px;
    letter-spacing: 0.02em;
    line-height: 1.55;
  }
  .contact__icon { width: 11px; height: 11px; flex: none; }
</style>
</head>
<body>
<main class="canvas">

  <section class="card card--front" aria-label="Card front">
    <div class="brand">
      <span class="brand__mark"></span>
      <div class="brand__text">
        <span class="brand__name">LumaMove</span>
        <span class="brand__tagline">In-home Personal Training</span>
      </div>
    </div>
  </section>

  <section class="card card--back" aria-label="Card back">
    <div class="brand">
      <span class="brand__mark"></span>
      <div class="brand__text">
        <span class="brand__name">LumaMove</span>
        <span class="brand__tagline">In-home Personal Training</span>
      </div>
    </div>
    <div class="card__rule"></div>

    <div class="contact">
      <p class="contact__name">Marta</p>
      <p class="contact__role">Director</p>
      <div class="contact__divider"></div>
      <p class="contact__line">
        <svg class="contact__icon" viewBox="0 0 24 24" aria-hidden="true">
          <path fill="currentColor" d="M6.6 10.8a15.1 15.1 0 0 0 6.6 6.6l2.2-2.2c.3-.3.7-.4 1-.2 1.1.4 2.3.6 3.6.6.6 0 1 .4 1 1V20c0 .6-.4 1-1 1C10.6 21 3 13.4 3 4c0-.6.4-1 1-1h3.5c.6 0 1 .4 1 1 0 1.3.2 2.5.6 3.6.1.3 0 .7-.2 1z"/>
        </svg>
        306-555-0187
      </p>
      <p class="contact__line">
        <svg class="contact__icon" viewBox="0 0 24 24" aria-hidden="true">
          <rect x="2.5" y="5" width="19" height="14" rx="1.5" fill="none" stroke="currentColor" stroke-width="2"/>
          <path d="M3 6l9 7 9-7" fill="none" stroke="currentColor" stroke-width="2"/>
        </svg>
        LumaMove.ca
      </p>
    </div>
  </section>

</main>
</body>
</html>
```